VELORAE is the product name. The product is a topical message oil for couples (his/her).

The package design needs to be erotic and classy. The design needs to carry over to the pump spray bottle. I already had a designed made for a similar product. I will include it as a sample but please do not copy it. Im looking for an original different design. However the oil, symbols are the same so use similar.
Requirements
Must have
- Only silver accents, no gold please. Thx

```html
<!DOCTYPE html>
<html lang="en">
<head>
<meta charset="utf-8">
<title>VELORAE – Massage Oil for Couples</title>
<link rel="stylesheet" href="https://fonts.googleapis.com/css2?family=Cormorant+Garamond:wght@300;400&family=Josefin+Sans:wght@300;400&display=swap">
<style>
  :root {
    --stage: #dcdcde;
    --stage-deep: #9d9d9f;
    --velvet-black: #0b0709;
    --velvet-wine: #3d0a18;
    --velvet-rose: #7a1a33;
    --blush: #b4475f;
    --silver-light: #f4f4f5;
    --silver-mid: #b8b8bc;
    --silver-dark: #5c5c60;
    --silver-ink: #d9d9dd;
    --silver-dim: #9a979b;
    --icon-ink: #2a1a20;
  }
  * { box-sizing: border-box; margin: 0; padding: 0; }
  html, body { width: 1200px; height: 959px; overflow: hidden; }
  body {
    background: linear-gradient(180deg, var(--stage) 0%, var(--stage-deep) 100%);
    font-family: "Josefin Sans", sans-serif;
    position: relative;
  }

  /* ---------- carton panels ---------- */
  .panel {
    position: absolute;
    top: 80px;
    height: 800px;
    text-align: center;
    overflow: hidden;
    color: var(--silver-ink);
  }
  .side-panel {
    left: 130px;
    width: 270px;
    background: linear-gradient(180deg, #140b0f 0%, var(--velvet-black) 100%);
    border-right: 1px solid rgba(217,217,221,.25);
  }
  .front-panel {
    left: 400px;
    width: 320px;
    background:
      radial-gradient(ellipse 70% 45% at 50% 50%, rgba(180,71,95,.45), transparent 72%),
      linear-gradient(180deg, var(--velvet-black) 0%, var(--velvet-wine) 45%, var(--velvet-rose) 60%, var(--velvet-wine) 78%, var(--velvet-black) 100%);
  }
  .silk {
    position: absolute;
    inset: 0;
    width: 100%;
    height: 100%;
  }
  .panel-frame {
    position: absolute;
    inset: 14px;
    border: 1px solid rgba(217,217,221,.45);
    pointer-events: none;
  }

  .brand-name {
    font-family: "Cormorant Garamond", serif;
    font-weight: 300;
    letter-spacing: .22em;
    color: var(--silver-light);
    position: relative;
  }
  .front-panel .brand-name { font-size: 44px; margin-top: 70px; padding-left: .22em; }
  .side-panel .brand-name { font-size: 32px; margin-top: 62px; padding-left: .22em; }

  .tagline {
    position: relative;
    font-weight: 300;
    font-size: 12px;
    letter-spacing: .32em;
    color: var(--silver-ink);
    margin-top: 12px;
  }
  .side-panel .tagline { font-size: 10px; color: var(--silver-dim); }

  .divider {
    position: relative;
    width: 60px;
    height: 1px;
    margin: 18px auto 0;
    background: var(--silver-mid);
  }

  .couple-rings {
    position: absolute;
    left: 50%;
    top: 290px;
    transform: translateX(-50%);
  }

  .audience {
    position: absolute;
    left: 0; right: 0;
    top: 470px;
    font-family: "Cormorant Garamond", serif;
    font-style: italic;
    font-weight: 300;
    font-size: 22px;
    letter-spacing: .08em;
    color: var(--silver-light);
  }

  .body-copy {
    position: relative;
    font-weight: 300;
    font-size: 12px;
    line-height: 1.55;
    color: var(--silver-dim);
    text-align: left;
    margin: 44px 32px 0;
  }
  .body-copy p + p { margin-top: 14px; }
  .body-copy .label { color: var(--silver-ink); letter-spacing: .12em; }

  .product-type {
    position: absolute;
    left: 0; right: 0;
    font-weight: 300;
    letter-spacing: .24em;
    color: var(--silver-light);
  }
  .front-panel .product-type { top: 610px; font-size: 13px; }
  .side-panel .product-type { top: 612px; font-size: 11px; color: var(--silver-ink); }

  .badges {
    position: absolute;
    left: 0; right: 0;
    display: flex;
    justify-content: center;
  }
  .front-panel .badges { top: 642px; gap: 12px; }
  .side-panel .badges { top: 642px; gap: 8px; }
  .badge { display: flex; flex-direction: column; align-items: center; gap: 6px; width: 58px; }
  .side-panel .badge { width: 50px; }
  .badge-caption { font-size: 10px; font-weight: 300; letter-spacing: .12em; color: var(--silver-ink); }
  .side-panel .badge-caption { font-size: 9px; color: var(--silver-dim); }

  .volume {
    position: absolute;
    left: 0; right: 0;
    top: 740px;
    font-size: 12px;
    font-weight: 300;
    letter-spacing: .2em;
    color: var(--silver-ink);
  }
  .side-panel .volume { font-size: 11px; color: var(--silver-dim); }

  /* ---------- pump bottle ---------- */
  .pump-bottle {
    position: absolute;
    left: 820px;
    top: 170px;
    width: 150px;
    height: 710px;
  }
  .bottle-nozzle {
    width: 40px;
    height: 20px;
    margin: 0 auto;
    border-radius: 4px 4px 0 0;
    background: linear-gradient(90deg, var(--silver-dark), var(--silver-light) 40%, var(--silver-mid) 70%, var(--silver-dark));
  }
  .bottle-cap,
  .bottle-base {
    background: linear-gradient(90deg, var(--silver-dark) 0%, var(--silver-light) 28%, var(--silver-mid) 52%, var(--silver-light) 74%, var(--silver-dark) 100%);
  }
  .bottle-cap { height: 210px; border-radius: 8px 8px 0 0; }
  .bottle-base { height: 100px; border-radius: 0 0 8px 8px; }
  .bottle-label {
    position: relative;
    height: 380px;
    overflow: hidden;
    background:
      linear-gradient(90deg, rgba(0,0,0,.45) 0%, transparent 30%, rgba(255,255,255,.08) 55%, rgba(0,0,0,.5) 100%),
      radial-gradient(ellipse 80% 45% at 50% 55%, rgba(180,71,95,.5), transparent 75%),
      linear-gradient(180deg, var(--velvet-black) 0%, var(--velvet-wine) 40%, var(--velvet-rose) 60%, var(--velvet-black) 100%);
    border-top: 2px solid var(--silver-mid);
    border-bottom: 2px solid var(--silver-mid);
  }
  .bottle-label .brand-name {
    position: absolute;
    left: 50%;
    top: 50%;
    font-size: 44px;
    letter-spacing: .2em;
    padding-left: .2em;
    white-space: nowrap;
    transform: translate(-50%, -50%) rotate(-90deg);
  }
  .bottle-label .product-type {
    position: absolute;
    left: auto; right: 14px;
    top: 50%;
    font-size: 9px;
    letter-spacing: .3em;
    white-space: nowrap;
    color: var(--silver-ink);
    transform: translate(50%, -50%) rotate(-90deg);
    transform-origin: center;
    width: 260px;
    margin-right: -120px;
  }
</style>
</head>
<body>

<svg width="0" height="0" style="position:absolute" aria-hidden="true">
  <defs>
    <linearGradient id="silver-stroke" x1="0" y1="0" x2="1" y2="1">
      <stop offset="0" stop-color="#f4f4f5"/>
      <stop offset=".5" stop-color="#9a9aa0"/>
      <stop offset="1" stop-color="#f4f4f5"/>
    </linearGradient>
    <symbol id="icon-natural" viewBox="0 0 40 40">
      <circle cx="20" cy="20" r="18" fill="#e9e9ec" stroke="#9a9aa0" stroke-width="2"/>
      <path d="M13 28 C14 18 20 12 29 11 C28 20 22 26 13 28 Z" fill="#2a1a20"/>
      <path d="M12 30 L22 19" stroke="#e9e9ec" stroke-width="1.4"/>
    </symbol>
    <symbol id="icon-vegan" viewBox="0 0 40 40">
      <circle cx="20" cy="20" r="18" fill="#e9e9ec" stroke="#9a9aa0" stroke-width="2"/>
      <path d="M20 29 L11 19 A5 5 0 0 1 20 14 A5 5 0 0 1 29 19 Z" fill="#2a1a20"/>
    </symbol>
    <symbol id="icon-pure" viewBox="0 0 40 40">
      <circle cx="20" cy="20" r="18" fill="#e9e9ec" stroke="#9a9aa0" stroke-width="2"/>
      <path d="M20 9 C24 16 27 20 27 24 A7 7 0 0 1 13 24 C13 20 16 16 20 9 Z" fill="#2a1a20"/>
    </symbol>
    <symbol id="icon-hemp" viewBox="0 0 40 40">
      <circle cx="20" cy="20" r="18" fill="#e9e9ec" stroke="#9a9aa0" stroke-width="2"/>
      <g fill="#2a1a20">
        <ellipse cx="20" cy="16" rx="2" ry="8"/>
        <ellipse cx="20" cy="16" rx="1.8" ry="7" transform="rotate(-40 20 24)"/>
        <ellipse cx="20" cy="16" rx="1.8" ry="7" transform="rotate(40 20 24)"/>
        <ellipse cx="20" cy="18" rx="1.5" ry="5" transform="rotate(-75 20 24)"/>
        <ellipse cx="20" cy="18" rx="1.5" ry="5" transform="rotate(75 20 24)"/>
      </g>
      <path d="M20 24 L20 30" stroke="#2a1a20" stroke-width="1.4"/>
    </symbol>
  </defs>
</svg>

<section class="panel side-panel">
  <svg class="silk" viewBox="0 0 270 800" preserveAspectRatio="none" aria-hidden="true">
    <path d="M-10 560 C80 520 160 600 280 540" fill="none" stroke="url(#silver-stroke)" stroke-width="1" opacity=".45"/>
    <path d="M-10 580 C90 545 170 620 280 565" fill="none" stroke="url(#silver-stroke)" stroke-width="1" opacity=".3"/>
  </svg>
  <div class="panel-frame"></div>
  <h2 class="brand-name">VELORAE</h2>
  <p class="tagline">AWAKEN THE SENSES</p>
  <div class="divider"></div>
  <div class="body-copy">
    <p>A silken blend of warming botanical oils, crafted for two. Glides smoothly over skin, melts at the touch and leaves a soft, lingering glow.</p>
    <p><span class="label">DIRECTIONS:</span> warm a few drops between your palms and massage slowly onto the body. For external use only.</p>
    <p><span class="label">INGREDIENTS:</span> sweet almond oil, jojoba oil, hemp seed oil, vitamin E, natural fragrance.</p>
  </div>
  <p class="product-type">TOPICAL MASSAGE OIL</p>
  <div class="badges">
    <div class="badge"><svg width="34" height="34"><use href="#icon-natural"/></svg><span class="badge-caption">NATURAL</span></div>
    <div class="badge"><svg width="34" height="34"><use href="#icon-vegan"/></svg><span class="badge-caption">VEGAN</span></div>
    <div class="badge"><svg width="34" height="34"><use href="#icon-pure"/></svg><span class="badge-caption">PURE</span></div>
    <div class="badge"><svg width="34" height="34"><use href="#icon-hemp"/></svg><span class="badge-caption">HEMP</span></div>
  </div>
  <p class="volume">30 ML</p>
</section>

<section class="panel front-panel">
  <svg class="silk" viewBox="0 0 320 800" preserveAspectRatio="none" aria-hidden="true">
    <path d="M-20 250 C60 200 120 330 200 300 S300 220 340 260" fill="none" stroke="url(#silver-stroke)" stroke-width="1.4" opacity=".55"/>
    <path d="M-20 275 C70 230 130 355 210 325 S305 250 340 290" fill="none" stroke="url(#silver-stroke)" stroke-width="1" opacity=".35"/>
    <path d="M-20 540 C50 580 140 500 220 540 S300 600 340 570" fill="none" stroke="url(#silver-stroke)" stroke-width="1.4" opacity=".55"/>
    <path d="M-20 565 C60 600 150 525 225 565 S305 620 340 598" fill="none" stroke="url(#silver-stroke)" stroke-width="1" opacity=".35"/>
  </svg>
  <div class="panel-frame"></div>
  <h1 class="brand-name">VELORAE</h1>
  <p class="tagline">AWAKEN THE SENSES</p>
  <div class="divider"></div>
  <svg class="couple-rings" width="170" height="130" viewBox="0 0 170 130" aria-hidden="true">
    <circle cx="62" cy="65" r="48" fill="none" stroke="url(#silver-stroke)" stroke-width="2.5"/>
    <circle cx="108" cy="65" r="48" fill="none" stroke="url(#silver-stroke)" stroke-width="2.5"/>
  </svg>
  <p class="audience">for him &amp; her</p>
  <p class="product-type">TOPICAL MASSAGE OIL</p>
  <div class="badges">
    <div class="badge"><svg width="42" height="42"><use href="#icon-natural"/></svg><span class="badge-caption">NATURAL</span></div>
    <div class="badge"><svg width="42" height="42"><use href="#icon-vegan"/></svg><span class="badge-caption">VEGAN</span></div>
    <div class="badge"><svg width="42" height="42"><use href="#icon-pure"/></svg><span class="badge-caption">PURE</span></div>
    <div class="badge"><svg width="42" height="42"><use href="#icon-hemp"/></svg><span class="badge-caption">HEMP</span></div>
  </div>
  <p class="volume">30 ML</p>
</section>

<div class="pump-bottle">
  <div class="bottle-nozzle"></div>
  <div class="bottle-cap"></div>
  <div class="bottle-label">
    <span class="brand-name">VELORAE</span>
  </div>
  <div class="bottle-base"></div>
</div>

</body>
</html>
```